Brisk Lyceum Website

We are looking for a new design of our website. The current website is www.brisklyceum-example.com. The company is the #1 pre-college math and science program in Orange County, CA. We would like to see designs that integrate our logo with a modern color scheme. We are also open for suggestions that could improve our logo. We would like a simple, minimal, clean, classy, and vibrant front-page user interface design that give the premium, modern, innovative, creative, and premier brand feel. We like the "New Retro Colors for the Web" as described here: http://www.pixelharbor-example.net/en/layout-notes-2013/.

Target Market(s)

The target market is parents with K-12 students from a diverse population. Parents are well educated with family income > $150,000. Most of the decision makers are mothers from immigrate families: 30% Chinese, 30% Korean, 15% Indian, 24% White.

Industry/Entity Type

College

Requirements
Must have
• Must read our statement of differentiation at:
• http://brisklyceum-example.com/about-us
• Your design must be reflective of your understanding of the statements.
Nice to have
• The design should also be mobil friendly.
Should not have
• While most of our current classes are math, our company is expanding to include STEM (Science, Technology, Engineering, and Math) for gifted students. Therefore, the site should not be JUST a math education site.

```html
<!DOCTYPE html>
<html lang="en">
<head>
<meta charset="utf-8">
<title>Brisk Lyceum – for Gifted Youth</title>
<link rel="stylesheet" href="https://fonts.googleapis.com/css2?family=Ubuntu:wght@300;400;500&display=swap">
<style>
:root{
  --teal:#2bb3bd;
  --yellow:#f3c22c;
  --red:#ea4f50;
  --navy:#123f8f;
  --green:#17904a;
  --orange:#f6a125;
  --brand-green:#7db462;
  --footer:#0b3b92;
  --text:#555;
  --dark:#222;
  --blue-text:#1d4f9c;
  --rule:#e4e4e4;
}
*{box-sizing:border-box;margin:0;padding:0}
html,body{width:932px;height:1200px;overflow:hidden;background:#fff}
body{font-family:"Ubuntu",sans-serif;color:var(--text);position:relative}
.page{position:relative;width:932px;height:1200px;overflow:hidden}
.top-bar{position:absolute;left:0;top:0;width:932px;height:4px;background:var(--brand-green)}

.brand{position:absolute;left:60px;top:24px;display:flex;align-items:center;gap:10px}
.brand-mark{width:48px;height:48px;border-radius:50%;background:var(--navy)}
.brand-name{font-size:25px;font-weight:400;color:var(--navy);line-height:1}
.brand-tag{font-size:13px;font-weight:300;color:var(--red);letter-spacing:2px;margin-top:3px}

.phone{position:absolute;right:52px;top:18px;display:flex;align-items:center;gap:4px;color:var(--brand-green);font-size:19px;font-weight:300}
.search{position:absolute;left:676px;top:51px;width:205px;height:27px;border:1px solid #ddd;display:flex;align-items:center;justify-content:space-between;padding:0 9px;font-size:10px;font-style:italic;color:#888}

.main-nav{position:absolute;left:47px;top:90px;width:838px;height:41px;display:flex;border-radius:6px 6px 0 0;overflow:hidden}
.main-nav a{flex:1;display:flex;align-items:center;justify-content:center;color:#fff;text-decoration:none;font-size:13px;font-weight:500}
.nav-teal{background:var(--teal)}.nav-yellow{background:var(--yellow)}.nav-red{background:var(--red)}
.nav-navy{background:var(--navy)}.nav-green{background:var(--green)}.nav-orange{background:var(--orange)}

.hero{position:absolute;left:47px;top:131px;width:838px;height:284px;background:linear-gradient(135deg,#d9c7a8 0%,#b58d66 40%,#6f5b4a 65%,#c9a286 100%)}
.hero-dots{position:absolute;left:50%;bottom:10px;transform:translateX(-50%);display:flex;gap:4px}
.hero-dots span{width:8px;height:8px;border-radius:50%;background:rgba(255,255,255,.75)}

.intro{position:absolute;left:47px;top:434px;width:838px;text-align:center}
.intro h1{font-size:23px;font-weight:400;color:var(--navy)}
.intro p{margin-top:8px;font-size:11.5px;font-weight:300;color:var(--blue-text);line-height:20px;padding:0 20px}

.features{position:absolute;left:47px;top:531px;width:843px;display:flex;gap:17px}
.feature{width:198px}
.feature-photo{height:107px;border-radius:4px}
.feature h2{font-size:17px;font-weight:400;margin:8px 2px 6px}
.feature p{font-size:10.5px;font-weight:300;line-height:18px;padding:0 2px;color:var(--text)}
.btn{display:inline-block;margin:9px 2px 0;width:87px;height:26px;line-height:26px;text-align:center;color:#fff;font-size:10.5px;border-radius:2px;text-decoration:none}
.c-teal{color:var(--teal)}.c-red{color:var(--red)}.c-navy{color:var(--navy)}.c-orange{color:var(--orange)}
.b-teal{background:var(--teal)}.b-red{background:var(--red)}.b-navy{background:var(--navy)}.b-orange{background:var(--orange)}

.divider{position:absolute;left:47px;top:788px;width:838px;height:1px;background:var(--rule)}

.col{position:absolute;top:824px}
.col h3{font-size:19px;font-weight:400;margin-bottom:14px}
.events{left:47px;width:270px}
.event{display:flex;gap:10px;margin-bottom:15px}
.event-photo{width:90px;height:84px;flex:none}
.event h4{font-size:13.5px;font-weight:400;color:var(--dark);margin-bottom:5px}
.event p{font-size:10.5px;font-weight:300;line-height:18px}
.learn{display:block;margin-top:5px;font-size:10px;color:var(--orange);text-decoration:none}

.programs{left:344px;width:270px}
.program-grid{display:grid;grid-template-columns:repeat(3,80px);gap:11px 13px}
.program-grid div{height:79px;border-radius:8px}

.news{left:642px;width:240px}
.news-item{margin-bottom:12px}
.news-item h4{font-size:11.5px;font-weight:400;color:var(--dark);margin-bottom:3px}
.news-item p{font-size:10px;font-weight:300;line-height:18px}

.site-footer{position:absolute;left:0;top:1097px;width:932px;height:103px;background:var(--footer);color:#fff}
.footer-links{position:absolute;left:54px;top:22px;font-size:11.5px}
.footer-links a{color:#fff;text-decoration:none}
.footer-links span{margin:0 5px}
.copyright{position:absolute;left:56px;top:52px;font-size:10px;font-weight:300}
.social{position:absolute;left:771px;top:25px;display:flex;gap:6px}
.social span{width:21px;height:21px;border-radius:3px;background:#3a8ee0}
</style>
</head>
<body>
<div class="page">
  <div class="top-bar"></div>

  <header>
    <div class="brand">
      <div class="brand-mark"></div>
      <div>
        <div class="brand-name">Brisk Lyceum</div>
        <div class="brand-tag">for Gifted Youth</div>
      </div>
    </div>
    <div class="phone">
      <svg width="18" height="18" viewBox="0 0 24 24"><path d="M6.6 10.8a15 15 0 0 0 6.6 6.6l2.2-2.2a1 1 0 0 1 1-.25 11.4 11.4 0 0 0 3.6.6 1 1 0 0 1 1 1V20a1 1 0 0 1-1 1A17 17 0 0 1 3 4a1 1 0 0 1 1-1h3.5a1 1 0 0 1 1 1c0 1.25.2 2.45.6 3.6a1 1 0 0 1-.25 1z" fill="#7db462"/></svg>
      (555).010.4477
    </div>
    <div class="search">
      <span>Search here..</span>
      <svg width="14" height="14" viewBox="0 0 16 16"><circle cx="6.5" cy="6.5" r="4.8" fill="none" stroke="#888" stroke-width="2"/><line x1="10" y1="10" x2="14.5" y2="14.5" stroke="#888" stroke-width="2.4" stroke-linecap="round"/></svg>
    </div>
  </header>

  <nav class="main-nav">
    <a class="nav-teal" href="#">HOME</a>
    <a class="nav-yellow" href="#">ABOUT US</a>
    <a class="nav-red" href="#">MATH</a>
    <a class="nav-navy" href="#">PHYSICS</a>
    <a class="nav-green" href="#">CHEMISTRY</a>
    <a class="nav-orange" href="#">BIOLOGY</a>
    <a class="nav-teal" href="#">SCIENCE FAIR</a>
    <a class="nav-yellow" href="#">FALL 2013</a>
  </nav>

  <section class="hero" role="img" aria-label="Photo of students working together in a classroom">
    <div class="hero-dots"><span></span><span></span><span></span><span></span></div>
  </section>

  <section class="intro">
    <h1>Why Brisk Lyceum for Gifted Youth?</h1>
    <p>Maecenas aliquet velit vel turpis. Mauris neque metus, malesuada nec, ultricies sit amet, porttitor mattis, enim. In massa libero, interdum nec, interdum vel, blandit sed, nulla. In ullamcorper, est eget tempor cursus, neque mi consectetuer mi</p>
  </section>

  <section class="features">
    <article class="feature">
      <div class="feature-photo" role="img" aria-label="Photo of smiling students at computers" style="background:linear-gradient(135deg,#c79a7a,#6b6f7a)"></div>
      <h2 class="c-teal">eLearning</h2>
      <p>Ut nisi erat, fermentum vel, congue id, euismod in, elit. Fusce ultricies</p>
      <a class="btn b-teal" href="#">READ MORE</a>
    </article>
    <article class="feature">
      <div class="feature-photo" role="img" aria-label="Photo of a globe and books on a desk before a chalkboard" style="background:linear-gradient(180deg,#2f8b76,#7aa894 60%,#a88b63)"></div>
      <h2 class="c-red">Scheduler</h2>
      <p>Ut nisi erat, fermentum vel, congue id, euismod in, elit. Fusce ultricies</p>
      <a class="btn b-red" href="#">READ MORE</a>
    </article>
    <article class="feature">
      <div class="feature-photo" role="img" aria-label="Photo of a hand reading news on a tablet" style="background:linear-gradient(135deg,#9a9a9a,#e3e3e3 55%,#555)"></div>
      <h2 class="c-navy">Newseltters</h2>
      <p>Ut nisi erat, fermentum vel, congue id, euismod in, elit. Fusce ultricies</p>
      <a class="btn b-navy" href="#">READ MORE</a>
    </article>
    <article class="feature">
      <div class="feature-photo" role="img" aria-label="Photo of a teacher with pupils raising hands" style="background:linear-gradient(135deg,#b89a6e,#e4d4b8 50%,#c89a7a)"></div>
      <h2 class="c-orange">Registration</h2>
      <p>Ut nisi erat, fermentum vel, congue id, euismod in, elit. Fusce ultricies</p>
      <a class="btn b-orange" href="#">READ MORE</a>
    </article>
  </section>

  <div class="divider"></div>

  <section class="col events">
    <h3 class="c-red">Upcoming Events</h3>
    <div class="event">
      <div class="event-photo" role="img" aria-label="Photo of children in a science lab wearing goggles" style="background:linear-gradient(135deg,#c7a88a,#8f8f8f)"></div>
      <div>
        <h4>Mauris vel lacus vitae felis</h4>
        <p>Phasellus felis dolor, scelerisque a, tempus eget, lobortis id, libero.</p>
        <a class="learn" href="#">LEARN MORE</a>
      </div>
    </div>
    <div class="event">
      <div class="event-photo" role="img" aria-label="Photo of a graduate in cap and gown" style="background:linear-gradient(135deg,#e8e8ec,#1b2a4a)"></div>
      <div>
        <h4>Proin nulla arcu</h4>
        <p>Phasellus felis dolor, scelerisque a, tempus eget, lobortis id, libero.</p>
        <a class="learn" href="#">LEARN MORE</a>
      </div>
    </div>
  </section>

  <section class="col programs">
    <h3 class="c-orange">Our Training &amp; Programs</h3>
    <div class="program-grid">
      <div role="img" aria-label="Photo of students at computers" style="background:linear-gradient(135deg,#d8d8d8,#4a4a4a)"></div>
      <div role="img" aria-label="Photo of a student with a lab flask" style="background:linear-gradient(135deg,#2a8a82,#b04a8a)"></div>
      <div role="img" aria-label="Photo of two smiling girls at a chalkboard" style="background:linear-gradient(135deg,#3e6e68,#e0b88e)"></div>
      <div role="img" aria-label="Photo of math written on a green chalkboard" style="background:linear-gradient(135deg,#1c7a5e,#0f5a45)"></div>
      <div role="img" aria-label="Photo of a laughing student in class" style="background:linear-gradient(135deg,#d6d6d6,#6a4a3a)"></div>
      <div role="img" aria-label="Photo of a lecture room with a projector" style="background:linear-gradient(135deg,#f0f0ee,#9a8a7a)"></div>
    </div>
  </section>

  <section class="col news">
    <h3 class="c-navy" style="color:var(--green)">Latest News &amp; Events</h3>
    <div class="news-item">
      <h4>Class aptent taciti sociosqu</h4>
      <p>Phasellus felis dolor, scelerisque a, tempus eget, lobortis id, libero Donec</p>
    </div>
    <div class="news-item">
      <h4>Donec iaculis diam</h4>
      <p>Phasellus felis dolor, scelerisque a, tempus eget, lobortis id, libero. Donec scelerisque</p>
    </div>
    <div class="news-item">
      <h4>Etiam eu urna</h4>
      <p>Phasellus felis dolor, scelerisque a, tempus eget, lobortis id, libero. Donec scelerisque leo</p>
    </div>
  </section>

  <footer class="site-footer">
    <div class="footer-links">
      <a href="#">Home</a><span>|</span><a href="#">About Us</a><span>|</span><a href="#">Services</a><span>|</span><a href="#">Subjects</a><span>|</span><a href="#">News</a><span>|</span><a href="#">Upcoming Events</a><span>|</span><a href="#">Sitemap</a><span>|</span><a href="#">Contact</a>
    </div>
    <div class="copyright">© 2013 Company Name. All right reserved. Term of Use</div>
    <div class="social"><span></span><span></span><span></span><span></span></div>
  </footer>
</div>
</body>
</html>
```